Bref créative |
Velmora Web Design | ||
Web Site design | ||
Telecommunications | ||
www.velmora-example.com | ||
Velmora is a US based independent telecom services company providing expertise to mobile network operators and network equipment vendors around the world. Our core services are constructed around our unique competencies in post-processing drive test data, coupled with our years of experience working with various wireless technologies, including GSM/GPRS/EDGE, UMTS/HSPA+ and LTE. Our mission is to enable network operators to achieve the maximum possible return on their investment in drive test data collection. Our website will be used primarily by clients to see if they want to do business with us, and as such needs to clearly convey our main services while creating an overall impression of professionalism and competence. |
Likes: Clarity & simpliciity Ease of navigation Dislikes: Clutter Pictures of random business people Links to Facebook & Twitter |
Cutting-Edge Clean/Simple Professional Modern High Tech |
Blue - see logo | ||
Black/White | ||
Anything that fits with the logo | ||
below header | ||
The Home page will have 4 links: About Services Clients Contact The Services page will contain links to pages detailing the various services we offer, around 7 or so. The design should be simple and streamlined, and be easy to navigate without any unnecessary clutter. The design should complement the attached logo. |

```html
<!DOCTYPE html>
<html lang="en">
<head>
<meta charset="utf-8">
<title>Velmora — Home</title>
<link href="https://fonts.googleapis.com/css2?family=Arimo:wght@400;700&family=Montserrat:wght@700;800&family=PT+Sans:ital,wght@0,400;0,700;1,400&display=swap" rel="stylesheet">
<style>
  :root {
    --white: #ffffff;
    --ink: #111111;
    --nav-blue: #0b3c9c;
    --deep: #05060c;
    --band-blue: #1433c8;
    --band-mid: #0a1a6a;
    --tile-light: #d9d9d9;
    --tile-dark: #8a8a8a;
    --grey-floor: #e4e4e4;
    --dot-on: #35d14a;
    --dot-off: #2b2b2b;
    --muted: #c8c8c8;
    --icon-grey: #6d6d6d;
  }
  * { margin: 0; padding: 0; box-sizing: border-box; }
  html, body { width: 1200px; height: 901px; overflow: hidden; background: var(--white); }
  .page { position: relative; width: 1200px; height: 901px; overflow: hidden; font-family: "Arimo", Arial, sans-serif; }

  .header { position: absolute; inset: 0 0 auto 0; height: 178px; background: var(--white); }
  .header-swoosh { position: absolute; inset: 0; }
  .brand { position: absolute; left: 30px; top: 56px; display: flex; align-items: center; gap: 14px; }
  .brand-mark { width: 52px; height: 52px; background: var(--nav-blue); }
  .brand-name { font-family: "Montserrat", sans-serif; font-weight: 800; font-size: 50px; letter-spacing: 1px; color: var(--ink); line-height: 1; }
  .brand-tagline { position: absolute; left: 30px; top: 136px; font-size: 13px; color: var(--ink); }

  .nav { position: absolute; top: 66px; left: 652px; display: flex; }
  .nav a { display: block; height: 36px; line-height: 36px; padding: 0 22px; font-weight: 700; font-size: 19px; color: var(--ink); text-decoration: none; letter-spacing: .5px; }
  .nav a.is-active { background: var(--nav-blue); color: var(--white); }

  .hero { position: absolute; top: 178px; left: 0; width: 1200px; height: 512px;
    background: linear-gradient(180deg, var(--deep) 0%, #070a22 30%, var(--band-mid) 62%, var(--band-blue) 100%); overflow: hidden; }
  .hero-swoosh { position: absolute; inset: 0; }

  .featured-title { position: absolute; left: 122px; top: 30px; font-family: "PT Sans", sans-serif; font-style: italic; font-weight: 700; font-size: 19px; letter-spacing: 1px; color: var(--white); text-decoration: underline; text-underline-offset: 5px; }

  .welcome { position: absolute; left: 470px; top: 150px; width: 650px; color: var(--white); }
  .welcome h1 { font-family: "PT Sans", sans-serif; font-weight: 700; font-size: 40px; letter-spacing: 2px; color: #e8e8e8; }
  .welcome .sub { font-family: "PT Sans", sans-serif; font-size: 22px; letter-spacing: 2px; color: var(--muted); margin-top: -4px; }
  .welcome p { margin-top: 38px; font-size: 17px; line-height: 1.25; text-align: justify; }

  .slider-dots { position: absolute; left: 745px; top: 452px; display: flex; gap: 16px; }
  .slider-dots span { width: 22px; height: 22px; border-radius: 50%; background: var(--dot-off); box-shadow: inset 0 1px 2px rgba(255,255,255,.2); }
  .slider-dots span.is-current { background: var(--dot-on); }

  .floor { position: absolute; top: 690px; left: 0; width: 1200px; height: 155px; background: linear-gradient(180deg, #f6f6f6, var(--grey-floor)); }
  .device-art { position: absolute; left: 784px; top: 40px; width: 178px; height: 108px; border-radius: 14px;
    background: linear-gradient(160deg, #f2f2f2 0%, #9fb4d8 45%, #1c4fb0 75%, #3a3a3a 100%); }
  .follow { position: absolute; left: 988px; top: 66px; font-family: "PT Sans", sans-serif; font-style: italic; font-size: 19px; color: #555; text-decoration: underline; }
  .social { position: absolute; left: 988px; top: 96px; display: flex; gap: 12px; }
  .social span { width: 44px; height: 44px; border-radius: 8px; background: var(--icon-grey); border: 3px solid #444; }
  .social span:last-child { background: var(--ink); }

  .service-grid { position: absolute; left: 66px; top: 260px; display: grid; grid-template-columns: 141px 141px; column-gap: 32px; row-gap: 31px; z-index: 2; }
  .service-tile { position: relative; width: 141px; height: 141px; border-radius: 12px;
    background: linear-gradient(180deg, var(--tile-light) 0%, #b3b3b3 55%, var(--tile-dark) 100%);
    box-shadow: 0 3px 8px rgba(0,0,0,.6), inset 0 1px 0 rgba(255,255,255,.8);
    display: flex; flex-direction: column; align-items: center; padding-top: 10px; }
  .service-tile svg { width: 72px; height: 62px; flex: none; }
  .service-label { margin-top: 6px; text-align: center; font-weight: 700; font-size: 13px; line-height: 1.15; color: var(--white); text-transform: uppercase;
    text-shadow: 0 0 2px #000, 0 1px 2px #000; padding: 0 4px; }
  .service-tile::after { content: ""; position: absolute; left: 10px; right: 10px; bottom: -22px; height: 14px; border-radius: 50%; background: rgba(0,0,0,.25); filter: blur(3px); }

  .footer { position: absolute; top: 845px; left: 0; width: 1200px; height: 56px; background: linear-gradient(180deg, #4a4a4a, #222); display: flex; align-items: center; justify-content: center; }
  .footer small { font-size: 10px; font-weight: 700; letter-spacing: 1px; color: var(--muted); }
</style>
</head>
<body>
<div class="page">
  <header class="header">
    <svg class="header-swoosh" viewBox="0 0 1200 178" preserveAspectRatio="none" aria-hidden="true">
      <path d="M360 178 C 620 120, 880 40, 1200 0 L1200 178 Z" fill="#efefef"/>
      <path d="M900 178 C 1000 120, 1100 70, 1200 40 L1200 178 Z" fill="#cfcfcf"/>
      <path d="M1050 178 C 1100 150, 1160 120, 1200 110 L1200 178 Z" fill="#b5b5b5"/>
    </svg>
    <div class="brand">
      <span class="brand-mark"></span>
      <span class="brand-name">VELMORA</span>
    </div>
    <div class="brand-tagline">Bringing your wireless data to life</div>
    <nav class="nav">
      <a class="is-active" href="#">ABOUT</a>
      <a href="#">SERVICES</a>
      <a href="#">CLIENTS</a>
      <a href="#">CONTACT</a>
    </nav>
  </header>

  <section class="hero">
    <svg class="hero-swoosh" viewBox="0 0 1200 512" preserveAspectRatio="none" aria-hidden="true">
      <path d="M420 512 C 600 300, 900 120, 1200 60 L1200 120 C 900 190, 660 340, 520 512 Z" fill="rgba(90,120,255,.18)"/>
      <path d="M620 512 C 760 360, 960 240, 1200 190 L1200 250 C 980 300, 820 400, 720 512 Z" fill="rgba(140,170,255,.14)"/>
      <path d="M0 380 C 300 330, 600 340, 1200 420 L1200 512 L0 512 Z" fill="rgba(30,70,255,.35)"/>
    </svg>

    <div class="featured-title">FEATURED SERVICES</div>

    <div class="welcome">
      <h1>WELCOME</h1>
      <div class="sub">LOREM IPSUM...</div>
      <p>Independant telecom services provider bringing innovations for real world technologies. Providing expertise to mobile network operators and network equipment vendors around the world.</p>
    </div>

    <div class="slider-dots"><span class="is-current"></span><span></span><span></span></div>
  </section>

  <section class="floor">
    <div class="device-art" role="img" aria-label="Illustration of a smartphone on a desk showing wireless data"></div>
    <div class="follow">Follow Us:</div>
    <div class="social"><span></span><span></span><span></span></div>
  </section>

  <div class="service-grid">
    <div class="service-tile">
      <svg viewBox="0 0 72 62" aria-hidden="true"><g fill="none" stroke="#222" stroke-width="3"><circle cx="28" cy="26" r="12"/><circle cx="28" cy="26" r="4"/><circle cx="50" cy="42" r="9"/><circle cx="50" cy="42" r="3"/><path d="M28 10v4M28 38v4M12 26h4M40 26h4M50 30v3M50 51v3M38 42h3M59 42h3"/></g></svg>
      <div class="service-label">Configured Virtual Solutions</div>
    </div>
    <div class="service-tile">
      <svg viewBox="0 0 72 62" aria-hidden="true"><g fill="none" stroke="#222" stroke-width="3"><rect x="12" y="6" width="48" height="48"/><path d="M28 6v48M44 6v48M12 22h48M12 38h48"/><path d="M14 50 L30 30 L42 36 L58 10" stroke-width="2.5"/></g></svg>
      <div class="service-label">Customized Reporting &amp; Optimization</div>
    </div>
    <div class="service-tile">
      <svg viewBox="0 0 72 62" aria-hidden="true"><g fill="none" stroke="#222" stroke-width="4"><circle cx="30" cy="26" r="16"/><path d="M42 38 L58 56" stroke-width="7" stroke-linecap="round"/></g></svg>
      <div class="service-label">Before/After Analysis</div>
    </div>
    <div class="service-tile">
      <svg viewBox="0 0 72 62" aria-hidden="true"><g fill="none" stroke="#222" stroke-width="3"><path d="M26 42 C 20 34, 18 30, 18 24 A18 18 0 0 1 54 24 C 54 30, 52 34, 46 42 Z"/><path d="M28 48h16M30 54h12"/></g></svg>
      <div class="service-label">Parameter Auditing/ Planning</div>
    </div>
    <div class="service-tile">
      <svg viewBox="0 0 72 62" aria-hidden="true"><g fill="#222"><path d="M10 40 L40 48 L62 36 L32 28 Z"/><path d="M10 32 L40 40 L62 28 L32 20 Z" fill="#444"/><path d="M10 24 L40 32 L62 20 L32 12 Z"/></g></svg>
      <div class="service-label">Benchmarking</div>
    </div>
    <div class="service-tile">
      <svg viewBox="0 0 72 62" aria-hidden="true"><g fill="none" stroke="#222" stroke-width="3" stroke-linejoin="round"><path d="M8 34 L64 10 L40 50 L32 38 Z"/><path d="M32 38 L64 10"/><path d="M6 50h20" stroke-width="2"/></g></svg>
      <div class="service-label">On-Site Deployment Services</div>
    </div>
  </div>

  <footer class="footer"><small>COPYRIGHT © 2012 VELMORA . ALL RIGHTS RESERVED.</small></footer>
</div>
</body>
</html>
```